Hair and Wellness Brochure and Pricelist design

I am requiring a brochure that has a fresh, though alternative design. My business name is The Quiet Harbor Hair and Wellness. I have a very professional approach to my work and love to give that little bit extra to all of my clients. My passion for health, has led me to channel my business alternatively by using non toxic colours and styling products and through that same vein, I have studied Aromatherapy, Indian Head Massage and Reiki...all additional services I use where required.
My studio has very neutral tones of beige,white and beech wood but these tones aren't necessarily required for the brochure.I like to create a space of calm, peace and quiet, where my clients feel refreshed and rejuvenated..

```html
<!DOCTYPE html>
<html lang="en">
<head>
<meta charset="utf-8">
<title>The Quiet Harbor Hair and Wellness – Price List</title>
<link href="https://fonts.googleapis.com/css2?family=Barlow:wght@400;500;600;700&display=swap" rel="stylesheet">
<style>
  :root {
    --page: #ffffff;
    --wood-light: #dcb39c;
    --wood-mid: #cfa58d;
    --wood-dark: #c0907a;
    --band: rgba(255, 255, 255, 0.45);
    --green-light: #9acd3c;
    --green-dark: #5e9e3a;
    --ink: #231f20;
    --fold: #6d5a50;
    --label: #222222;
    --photo-light: #f3ead8;
    --photo-warm: #e8cdb4;
    --leaf-light: rgba(200, 227, 108, 0.85);
    --leaf-dark: rgba(95, 158, 44, 0.9);
  }
  * { margin: 0; padding: 0; box-sizing: border-box; }
  html, body { width: 1200px; height: 1000px; overflow: hidden; background: var(--page); }
  body { position: relative; font-family: "Barlow", Arial, sans-serif; color: var(--ink); }

  .panel-label {
    position: absolute; top: 37px; width: 300px; text-align: center;
    font-size: 15px; font-weight: 400; letter-spacing: 0.5px; color: var(--label);
  }

  .spread {
    position: absolute; left: 50px; top: 73px; width: 1100px; height: 854px; overflow: hidden;
    background:
      repeating-linear-gradient(180deg, transparent 0 72px, rgba(120, 70, 50, 0.06) 72px 74px),
      linear-gradient(160deg, var(--wood-light) 0%, var(--wood-mid) 55%, var(--wood-dark) 100%);
  }

  .band { position: absolute; background: var(--band); }
  .band--top { left: 0; top: 126px; width: 940px; height: 47px;
    background: linear-gradient(90deg, var(--band) 85%, rgba(255,255,255,0)); }
  .band--bottom { left: 0; top: 634px; width: 460px; height: 118px;
    background: linear-gradient(90deg, var(--band) 80%, rgba(255,255,255,0)); }

  .foliage {
    position: absolute; right: 0; top: 0; width: 460px; height: 480px;
    background: radial-gradient(ellipse at 100% 0%, var(--leaf-dark) 0%, var(--leaf-light) 45%, rgba(200,227,108,0) 72%);
  }
  .photo {
    position: absolute; left: 740px; top: 215px; width: 360px; height: 639px;
    background: linear-gradient(160deg, var(--photo-light) 0%, var(--photo-warm) 100%);
  }

  .fold { position: absolute; top: 0; height: 854px; border-left: 1px dashed var(--fold); opacity: 0.8; }

  .ribbon { position: absolute; left: 48px; top: 124px; width: 262px; height: 47px; }
  .ribbon__text {
    position: absolute; left: 48px; top: 124px; width: 262px; height: 47px;
    display: flex; align-items: center; justify-content: center;
    color: #fff; font-weight: 700; font-size: 23px; letter-spacing: 0.5px;
  }

  .note { position: absolute; left: 434px; top: 134px; font-size: 13px; font-weight: 600; line-height: 16px; letter-spacing: 0.2px; }

  .section { position: absolute; width: 236px; font-weight: 600; font-size: 13px; line-height: 16px; letter-spacing: 0.2px; }
  .section__title { font-size: 16px; font-weight: 700; letter-spacing: 0.3px; line-height: 22px; margin-bottom: 2px; }
  .item { margin-bottom: 6px; }
  .row { display: flex; align-items: baseline; }
  .row__leader { flex: 1; border-bottom: 2px dotted var(--ink); margin: 0 4px 3px 2px; opacity: 0.85; }
  .row__price { white-space: nowrap; }

  .cuts { left: 69px; top: 214px; }
  .colour { left: 69px; top: 361px; }
  .other { left: 434px; top: 214px; }
  .wedding { left: 434px; top: 312px; }

  .brand { position: absolute; left: 62px; top: 652px; display: flex; align-items: center; gap: 16px; }
  .brand__mark { width: 72px; height: 72px; border-radius: 50%;
    background: linear-gradient(90deg, var(--green-light), var(--green-dark)); flex: none; }
  .brand__name { color: var(--green-dark); font-weight: 700; font-size: 16px; line-height: 20px; letter-spacing: 0.4px; }
</style>
</head>
<body>
  <div class="panel-label" style="left:83px">INSIDE LEFT</div>
  <div class="panel-label" style="left:448px">INSIDE CENTRE</div>
  <div class="panel-label" style="left:815px">INSIDE RIGHT</div>

  <main class="spread">
    <div class="band band--top"></div>
    <div class="band band--bottom"></div>

    <div class="foliage" role="img" aria-label="Photo of green tree leaves in the top right corner"></div>
    <div class="photo" role="img" aria-label="Photo of a woman with long straight blonde hair"></div>

    <div class="fold" style="left:366px"></div>
    <div class="fold" style="left:731px"></div>

    <svg class="ribbon" viewBox="0 0 262 47" aria-hidden="true">
      <defs>
        <linearGradient id="ribbonGreen" x1="0" x2="1">
          <stop offset="0" stop-color="#9acd3c"/>
          <stop offset="1" stop-color="#5e9e3a"/>
        </linearGradient>
      </defs>
      <path d="M0 2 H262 L254 23.5 L262 45 H0 L8 23.5 Z" fill="url(#ribbonGreen)"/>
      <line x1="12" y1="6" x2="250" y2="6" stroke="#fff" stroke-width="1" stroke-dasharray="3 2"/>
      <line x1="12" y1="41" x2="250" y2="41" stroke="#fff" stroke-width="1" stroke-dasharray="3 2"/>
    </svg>
    <div class="ribbon__text">PRICE LIST</div>

    <p class="note">All services include a soothing<br>aromatherapy neck massage</p>

    <section class="section cuts">
      <h2 class="section__title">CUTS</h2>
      <div class="item"><div class="row"><span>Shampoo &amp; blow dry</span><span class="row__leader"></span><span class="row__price">$40</span></div></div>
      <div class="item">Hot tool styling with Shampoo<div class="row"><span>included</span><span class="row__leader"></span><span class="row__price">$50</span></div></div>
      <div class="item"><div class="row"><span>Shampoo cut &amp; blow dry</span><span class="row__leader"></span><span class="row__price">$70</span></div></div>
      <div class="item"><div class="row"><span>Men’s style cut</span><span class="row__leader"></span><span class="row__price">$30</span></div></div>
    </section>

    <section class="section colour">
      <h2 class="section__title">COLOUR</h2>
      <div class="item">Tint &amp; semi permanent<div class="row"><span>regrowth colour</span><span class="row__leader"></span><span class="row__price">$60</span></div></div>
      <div class="item"><div class="row"><span>Half head foils</span><span class="row__leader"></span><span class="row__price">$60</span></div></div>
      <div class="item"><div class="row"><span>Full head foils</span><span class="row__leader"></span><span class="row__price">$120</span></div></div>
      <div class="item">Any additional colour<div class="row"><span>starts from</span><span class="row__leader"></span><span class="row__price">$20</span></div></div>
      <div class="item">Corrective colour services are priced<br>at consultation</div>
    </section>

    <section class="section other">
      <h2 class="section__title">OTHER SERVICES</h2>
      <div class="item">45 minute Indian Head Massage<br>with a Reiki and<div class="row"><span>Aromatherapy Infusion</span><span class="row__leader"></span><span class="row__price">$50</span></div></div>
    </section>

    <section class="section wedding">
      <h2 class="section__title">WEDDING AND FORMAL<br>CONSULTATIONS</h2>
      <div class="item">Hair up styling including<div class="row"><span>the use of hot tools</span><span class="row__leader"></span><span class="row__price">$50</span></div></div>
      <div class="item">All wedding hairstyling<div class="row"><span>starts from</span><span class="row__leader"></span><span class="row__price">$60</span></div>(Price on consultation)</div>
      <div class="item"><div class="row"><span>Wedding up style consultation</span><span class="row__leader"></span><span class="row__price">$50</span></div></div>
    </section>

    <div class="brand">
      <span class="brand__mark" aria-hidden="true"></span>
      <p class="brand__name">THE QUIET HARBOR<br>HAIR &amp; WELLNESS</p>
    </div>
  </main>
</body>
</html>
```